PDF-Dokumente für Vermietung und Verwaltung von Immobilien
Zielgruppe
WohnKranich, Vermietung und Verwaltung von Immoblien
Aufgabenstellung
Wir haben ganz viele Dokumente, die als PDF erstellt werden sollen, Einheitlich im CI Design, mit Logo etc. Manche PDFS müssen ausfüllbar sein andere sind einfach nur zum Drucken. es sind ca 10-20 Word/PDF Dokumente.

```html
<!DOCTYPE html>
<html lang="de">
<head>
<meta charset="utf-8">
<title>Bürgschaftsurkunde – WohnKranich</title>
<link href="https://fonts.googleapis.com/css2?family=Carlito:wght@400;700&display=swap" rel="stylesheet">
<style>
  :root {
    --navy: #0f1f3a;
    --ink: #111111;
    --paper: #ffffff;
    --rule: #1a1a1a;
  }
  * { margin: 0; padding: 0; box-sizing: border-box; }
  html, body { width: 849px; height: 1200px; overflow: hidden; background: var(--paper); }
  .page {
    position: relative;
    width: 849px;
    height: 1200px;
    font-family: "Carlito", "Calibri", sans-serif;
    color: var(--ink);
    background: var(--paper);
    overflow: hidden;
  }
  .brand {
    position: absolute;
    top: 100px;
    left: 0;
    width: 849px;
    text-align: center;
    font-size: 26px;
    font-weight: 400;
    letter-spacing: 1px;
    color: var(--navy);
  }
  .doc-title {
    position: absolute;
    left: 72px;
    top: 222px;
    width: 445px;
    height: 40px;
    background: var(--navy);
    color: #fff;
    font-size: 20.5px;
    line-height: 40px;
    padding-left: 12px;
    letter-spacing: 0.4px;
  }
  .label {
    position: absolute;
    left: 72px;
    font-size: 14px;
    line-height: 1;
  }
  .rule {
    position: absolute;
    height: 1px;
    background: var(--rule);
  }
  .section-head {
    position: absolute;
    left: 72px;
    top: 569px;
    font-size: 16.5px;
    font-weight: 700;
  }
  .terms {
    position: absolute;
    left: 72px;
    top: 711px;
    font-size: 14px;
    line-height: 19.95px;
    white-space: nowrap;
  }
  .sig-label {
    position: absolute;
    top: 993px;
    font-size: 14px;
  }
  .footer-band {
    position: absolute;
    left: 0;
    top: 1175px;
    width: 849px;
    height: 25px;
  }
</style>
</head>
<body>
<main class="page">
  <div class="brand">WohnKranich</div>

  <h1 class="doc-title">Bürgschaftsurkunde für das Mietverhältnis</h1>

  <div class="label" style="top:316px">zwischen dem Vermieter</div>
  <div class="rule" style="left:248px;width:529px;top:328px"></div>
  <div class="rule" style="left:248px;width:529px;top:357px"></div>

  <div class="label" style="top:402px">und dem Mieter</div>
  <div class="rule" style="left:194px;width:583px;top:414px"></div>
  <div class="rule" style="left:194px;width:583px;top:443px"></div>

  <div class="label" style="top:487px">für das Mietobjekt</div>
  <div class="rule" style="left:209px;width:568px;top:500px"></div>

  <h2 class="section-head">Hiermit übernehme ich</h2>

  <div class="label" style="top:609px">Vorname, Nachname</div>
  <div class="rule" style="left:225px;width:552px;top:622px"></div>
  <div class="label" style="top:638px">Anschrift:</div>
  <div class="rule" style="left:152px;width:625px;top:650px"></div>
  <div class="label" style="top:666px">Geboren am, in</div>
  <div class="rule" style="left:189px;width:588px;top:679px"></div>

  <p class="terms">
    die unbefristete, freiwillige und selbstschuldnerische Bürgschaft für den o. g. Mieter in dem o. g. Mietverhältnis.<br>
    Die Bürgschaft gilt für alle Mietzinsansprüche, Nachzahlung von Betriebskosten aus der jeweiligen Abrechnung<br>
    und einer evtl. stillschweigenden Verlängerung des Mietverhältnisses. Bei dieser Bürgschaft handelt es sich<br>
    um eine freiwillige, selbstschuldnerische Bürgschaft, die die Zahlung einer Mietkaution nicht ersetzt. Die<br>
    Bürgschaft gilt über die Kündigung, gemäß § 568 BGB, hinaus.<br>
    Ich verzichte ausdrücklich auf mir nach dem Gesetz zustehende Einreden, insbesondere auf die Einrede der<br>
    Anfechtung, der Aufrechnung und der Vorausklage und der Hinterlegung gemäß § § 770, 771 BGB.<br>
    Dieser Bürgschaftsurkunde lege ich eine Kopie meines Personalausweises bei.
  </p>

  <div class="rule" style="left:72px;width:262px;top:987px"></div>
  <div class="sig-label" style="left:72px">Ort, Datum</div>
  <div class="rule" style="left:435px;width:322px;top:987px"></div>
  <div class="sig-label" style="left:435px">Unterschrift des Bürgen</div>

  <svg class="footer-band" viewBox="0 0 849 25" aria-hidden="true">
    <rect width="849" height="25" fill="var(--navy)"/>
    <polygon points="644,0 653,0 643,25 634,25" fill="var(--paper)"/>
  </svg>
</main>
</body>
</html>
```